Personal Training Company
Summit Vigor & Fitness
Project: Personal Training Company
Personal Training Company - Health
Creative Brief
Professional
Dara Morlane, MS, CPT, CNC
Brookvale, NC
summitvandfit@brivomail.com
tekrin27 tekrin27
I Can make all the changes you want and if you want to add anything in your card after the contest. I will do that free

```html
<!DOCTYPE html>
<html lang="en">
<head>
<meta charset="utf-8">
<title>Summit Vigor &amp; Fitness – Business Card</title>
<link rel="stylesheet" href="https://fonts.googleapis.com/css2?family=Montserrat:wght@400;600;800&family=Open+Sans:wght@400;600&display=swap">
<style>
  :root {
    --stage: #2a2a2b;
    --card-white: #ffffff;
    --card-dark: #4f5052;
    --card-dark-edge: #3e3f41;
    --ink-dark: #4a4a4a;
    --ink-light: #ffffff;
    --muted-light: #d9d9d9;
    --accent: #9ccc2f;
  }
  * { margin: 0; padding: 0; box-sizing: border-box; }
  html, body { width: 1200px; height: 901px; overflow: hidden; }
  body {
    background: var(--stage);
    position: relative;
    font-family: "Open Sans", Arial, sans-serif;
  }
  .card {
    position: absolute;
    width: 560px;
    height: 320px;
    border-radius: 4px;
    box-shadow: 0 18px 40px rgba(0,0,0,0.45);
    overflow: hidden;
  }
  .card-front { left: 110px; top: 110px; background: var(--card-white); }
  .card-back {
    left: 530px; top: 470px;
    background: linear-gradient(135deg, var(--card-dark) 0%, var(--card-dark-edge) 100%);
    color: var(--ink-light);
  }
  .brand { position: absolute; display: flex; align-items: center; gap: 16px; }
  .card-front .brand { left: 70px; top: 92px; }
  .brand-dot {
    width: 74px; height: 74px; border-radius: 50%;
    background: var(--ink-dark);
    flex-shrink: 0;
  }
  .brand-name {
    font-family: "Montserrat", Arial, sans-serif;
    font-weight: 800;
    font-size: 30px;
    line-height: 1.05;
    text-transform: uppercase;
    color: var(--ink-dark);
    white-space: nowrap;
  }
  .tagline {
    font-family: "Montserrat", Arial, sans-serif;
    font-weight: 600;
    font-size: 9.5px;
    letter-spacing: 0.6px;
    text-transform: uppercase;
    margin-top: 6px;
    white-space: nowrap;
  }
  .card-front .tagline { color: var(--ink-dark); }
  .website {
    position: absolute; left: 0; right: 0; bottom: 56px;
    text-align: center;
    font-size: 13px; letter-spacing: 3px;
    color: var(--ink-dark);
  }
  .card-back .brand { left: 38px; top: 64px; }
  .card-back .brand-name { color: var(--ink-light); font-size: 32px; }
  .card-back .tagline { color: var(--muted-light); }
  .accent-bar {
    position: absolute; left: 38px; top: 52px;
    width: 60px; height: 3px; background: var(--accent);
  }
  .contact { position: absolute; left: 38px; top: 178px; }
  .person-name {
    font-family: "Montserrat", Arial, sans-serif;
    font-weight: 600; font-size: 17px;
  }
  .credentials { font-size: 12px; margin: 3px 0 10px; color: var(--muted-light); }
  .contact-line {
    display: flex; align-items: center; gap: 8px;
    font-size: 11.5px; color: var(--muted-light);
    margin-top: 5px;
    white-space: nowrap;
  }
  .contact-line svg { width: 12px; height: 12px; flex-shrink: 0; }
</style>
</head>
<body>
  <section class="card card-front">
    <div class="brand">
      <span class="brand-dot"></span>
      <div>
        <div class="brand-name">Summit Vigor<br>&amp; Fitness</div>
        <div class="tagline">Stronger every day, one step at a time</div>
      </div>
    </div>
    <div class="website">www.summitvandf.com</div>
  </section>

  <section class="card card-back">
    <span class="accent-bar"></span>
    <div class="brand">
      <div>
        <div class="brand-name">Summit Vigor &amp; Fitness</div>
        <div class="tagline">Stronger every day, one step at a time</div>
      </div>
    </div>
    <div class="contact">
      <div class="person-name">Dara Morlane</div>
      <div class="credentials">MS, CPT, CNC</div>
      <div class="contact-line">Brookvale, NC</div>
      <div class="contact-line">
        <svg viewBox="0 0 12 12" aria-hidden="true"><rect x="3" y="0.5" width="6" height="11" rx="1.2" fill="none" stroke="#d9d9d9" stroke-width="1"/><circle cx="6" cy="9.6" r="0.7" fill="#d9d9d9"/></svg>
        704-555-0182
      </div>
      <div class="contact-line">
        <svg viewBox="0 0 12 12" aria-hidden="true"><rect x="0.5" y="2.5" width="11" height="7" rx="1" fill="none" stroke="#d9d9d9" stroke-width="1"/><path d="M0.8 3 L6 7 L11.2 3" fill="none" stroke="#d9d9d9" stroke-width="1"/></svg>
        summitvandfit@brivomail.com
      </div>
    </div>
  </section>
</body>
</html>
```